New Fernwick 4 Loop waste management business seeking web site

New project for business offering sustainable options within the waste industry.
Business called Fernwick 4 Loop
Targeting the consumer & industry professionals the web site needs to be able to accommodate both.
Needs to have a modern clean feel.
Logo being designed by another pro and will be completed early next week and will be submitted soon after to be incorporated into the web page
Links to another web page i like very much to take into consideration.

Target Market(s)

Industry professionals, consumers and producers of all waste, Food, constructruction, commercial, retail .. etc..

Industry/Entity Type

Waste Management

Coding

Coded - Design and coding required

Number of Pages Required

5+ page

Font styles to use
Serif
Script

Requirements
Must have
• Flexabilty, all pages as in examples
Nice to have
• Open to offers you guys and gals are the pro's

```html
<!DOCTYPE html>
<html lang="en">
<head>
<meta charset="utf-8">
<title>Fernwick 4 Loop – Recovery &amp; Recycling</title>
<link href="https://fonts.googleapis.com/css2?family=Lato:wght@400;700&family=Raleway:wght@400;600;700;800&family=Dancing+Script:wght@600&display=swap" rel="stylesheet">
<style>
:root{
  --green:#4a7d05;
  --green-light:#5f9a12;
  --green-soft:#8fb35a;
  --dark:#252525;
  --ink:#1e1e1e;
  --text:#555;
  --grey-bg:#f1f1f1;
  --line:#cfcfcf;
  --white:#fff;
}
*{margin:0;padding:0;box-sizing:border-box}
html,body{width:1200px;height:2528px;overflow:hidden}
body{font-family:"Lato",sans-serif;color:var(--text);background:var(--white);position:relative}
section,header,footer,nav{position:absolute;left:0;width:1200px}
.inner{position:absolute}

/* top bar */
.topbar{top:0;height:71px;background:var(--white);z-index:1}
.phone{left:130px;top:18px;display:flex;align-items:center;gap:12px;font-size:19px;line-height:24px;color:var(--green);white-space:nowrap}
.search{left:862px;top:19px;width:206px;height:30px;border:1px solid #d6d6d6;background:#fafafa;font-size:12px;color:#777;padding:7px 12px;display:flex;justify-content:space-between;align-items:center}

/* nav */
.nav{top:71px;height:60px;background:var(--green);border-top:2px dashed #c9d9b3;z-index:2}
.nav ul{list-style:none;display:flex;position:absolute;top:0;height:58px}
.nav li{color:var(--white);font-size:16px;padding:0 18px;line-height:58px;border-left:1px solid rgba(255,255,255,.25);white-space:nowrap}
.nav .left{left:130px}
.nav .right{left:700px}
.nav .right li:last-child{border-right:1px solid rgba(255,255,255,.25)}
.brand{position:absolute;left:514px;top:64px;width:172px;height:112px;border-radius:0 0 86px 86px;background:var(--white);border:2px dashed #c9d9b3;border-top:none;display:flex;flex-direction:column;align-items:center;justify-content:center;z-index:3}
.brand .dot{width:26px;height:26px;border-radius:50%;background:var(--green);margin-bottom:6px}
.brand .name{font-family:"Lato",sans-serif;font-weight:700;font-size:17px;color:var(--green);white-space:nowrap}

/* hero */
.hero{top:131px;height:466px;background:linear-gradient(180deg,#3f6fb5 0%,#8eaed8 40%,#bfb3a0 62%,#8d8272 100%)}
.hero .caption{position:absolute;left:0;bottom:0;width:1200px;height:52px;background:rgba(40,40,40,.65);text-align:center;font-family:"Dancing Script",cursive;font-size:33px;color:var(--white);line-height:52px}

/* section headings */
.heading{position:absolute;left:0;width:1200px;text-align:center;font-family:"Raleway",sans-serif;font-weight:800;font-size:27px;color:var(--ink);letter-spacing:.5px}
.heading span{color:var(--green)}
.divider{position:absolute;left:50%;transform:translateX(-50%);height:20px;display:flex;align-items:center}
.divider i{display:block;height:3px;border-top:1px solid var(--line);border-bottom:1px solid var(--line)}
.divider b{display:block;width:18px;height:18px;border-radius:50%;background:var(--green);margin:0 10px}

/* process */
.process{top:597px;height:474px;background:var(--grey-bg)}
.step{position:absolute;top:158px;width:190px;text-align:center}
.step .ring{width:190px;height:190px;border-radius:50%;background:var(--white);box-shadow:0 2px 6px rgba(0,0,0,.12);display:flex;align-items:center;justify-content:center}
.step .disc{width:168px;height:168px;border-radius:50%;background:var(--green);border:2px dashed rgba(255,255,255,.55);outline:6px solid var(--green);outline-offset:-8px;display:flex;align-items:center;justify-content:center}
.step .label{margin:38px -40px 0;font-family:"Lato",sans-serif;font-size:22px;color:var(--ink);white-space:nowrap}
.step .bar{width:46px;height:4px;background:var(--green-soft);margin:14px auto 0}
.flow{position:absolute}

/* welcome */
.welcome{top:1071px;height:340px;background:var(--white)}
.welcome p{position:absolute;left:140px;top:126px;width:920px;text-align:center;font-family:"Raleway",sans-serif;font-size:14.5px;line-height:31px;color:#555}
.btn-more{position:absolute;left:536px;top:269px;display:flex;height:34px}
.btn-more .txt{background:var(--green);color:var(--white);font-size:14px;padding:0 10px;line-height:34px}
.btn-more .arr{width:36px;background:#1a1a1a;color:var(--white);line-height:34px;text-align:center;font-size:16px}

/* services */
.services{top:1411px;height:399px;background:var(--grey-bg)}
.service{position:absolute;top:142px;width:282px;height:218px;background:var(--white);box-shadow:0 2px 5px rgba(0,0,0,.2);padding:6px}
.service .photo{width:270px;height:152px}
.service .title{position:absolute;left:0;bottom:0;width:282px;height:56px;background:var(--green);border:2px dashed rgba(255,255,255,.6);outline:3px solid var(--green);outline-offset:-3px;color:var(--white);font-size:24px;text-align:center;line-height:52px;white-space:nowrap}
.chev{position:absolute;top:217px}

/* blog */
.blog{top:1810px;height:380px;background:var(--white)}
.post{position:absolute;top:136px;width:452px;height:206px;background:#f5f5f5;border:1px solid #cfcfcf;box-shadow:0 3px 5px rgba(0,0,0,.2)}
.post .photo{position:absolute;left:7px;top:7px;width:186px;height:190px}
.post .body{position:absolute;left:212px;top:10px;width:228px}
.post h3{font-family:"Lato",sans-serif;font-weight:700;font-size:19px;color:var(--green)}
.post .date{display:flex;align-items:center;gap:10px;font-size:15px;color:#333;margin-top:10px}
.post p{font-size:13px;line-height:20px;color:#444;margin-top:12px}
.post .read{display:inline-block;margin-top:18px;border:2px solid var(--green);border-radius:3px;color:var(--green);font-size:15px;padding:5px 20px}

/* footer */
.footer{top:2190px;height:298px;background:var(--dark);border-top:3px solid var(--green);color:#ddd}
.col{position:absolute;top:34px}
.col h4{font-size:16px;font-weight:700;color:var(--white);padding-bottom:10px;border-bottom:1px dashed #666;width:128px}
.links{list-style:none;margin-top:12px}
.links li{font-size:13px;line-height:26px}
.links li::before{content:"›";margin-right:10px;color:#aaa}
.col p{font-size:13px;line-height:20px;margin-top:14px}
.email-box{margin-top:16px;width:248px;height:34px;background:var(--white);border-radius:3px;color:#444;font-size:12px;display:flex;align-items:center;gap:10px;padding:0 12px}
.subscribe{margin-top:16px;display:inline-block;background:var(--green-light);color:var(--white);font-size:12px;font-weight:700;padding:9px 12px;border-radius:2px}
.contact-row{display:flex;align-items:center;gap:12px;font-size:13px;margin-top:12px}
.social{list-style:none;margin-top:14px}
.social li{display:flex;align-items:center;gap:12px;font-size:13px;line-height:24px;margin-bottom:13px}
.social .sq{width:24px;height:24px;background:#e6e6e6;border-radius:2px}
.bottombar{position:absolute;left:0;width:1200px;top:2488px;height:40px;background:var(--green);color:var(--white);font-size:12px}
.bottombar .copy{left:132px;top:13px}
.bottombar .legal{left:872px;top:13px}
</style>
</head>
<body>

<header class="topbar">
  <div class="inner phone">
    <svg width="22" height="22" viewBox="0 0 22 22"><circle cx="11" cy="11" r="10" fill="none" stroke="#4a7d05" stroke-width="1.6"/><path d="M7.5 6.5c.5-.5 1.2-.5 1.6 0l1 1.3c.3.4.2 1-.2 1.3l-.6.5c.6 1.3 1.6 2.3 2.9 2.9l.5-.6c.3-.4.9-.5 1.3-.2l1.3 1c.5.4.5 1.1 0 1.6l-.7.7c-3.5-.3-7.5-4.3-7.8-7.8z" fill="#4a7d05"/></svg>
    <span>555-010-2468</span>
  </div>
  <div class="inner search">
    <span>Search</span>
    <svg width="13" height="13" viewBox="0 0 13 13"><circle cx="5.5" cy="5.5" r="4" fill="none" stroke="#4a7d05" stroke-width="2"/><path d="M8.5 8.5l3.5 3.5" stroke="#4a7d05" stroke-width="2"/></svg>
  </div>
</header>

<nav class="nav">
  <ul class="left"><li>Home</li><li>About</li><li>Services</li><li>Insight</li></ul>
  <ul class="right"><li>Work</li><li>Collaborations</li><li>Blog</li><li>Contact</li></ul>
</nav>
<div class="brand"><span class="dot"></span><span class="name">Fernwick 4 Loop</span></div>

<section class="hero" role="img" aria-label="Photo of an orange excavator arm over piles of crushed concrete rubble under a blue sky">
  <div class="caption">Our business offering sustainable options within the Waste Industry.</div>
</section>

<section class="process">
  <h2 class="heading" style="top:40px">HOW IT <span>WORK</span></h2>
  <div class="divider" style="top:88px"><i style="width:136px"></i><b></b><i style="width:136px"></i></div>

  <svg class="flow" style="left:300px;top:148px" width="600" height="140" viewBox="0 0 600 140" fill="none" stroke="#c9cfbf" stroke-width="2">
    <path d="M6 16c30-12 60-12 86-4"/><path d="M84 4l10 8-12 5"/>
    <path d="M250 124c30 10 60 8 82-6"/><path d="M322 112l12 4-8 10"/>
    <path d="M500 16c30-12 56-12 80-4"/><path d="M572 4l10 8-12 5"/>
  </svg>

  <div class="step" style="left:133px">
    <div class="ring"><div class="disc">
      <svg width="120" height="80" viewBox="0 0 120 80" fill="#fff"><path d="M4 32h16v-10l16 18-16 18v-10H4z"/><rect x="46" y="14" width="44" height="6" rx="2"/><rect x="60" y="8" width="16" height="6" rx="2"/><path d="M49 22h38l-4 50H53z"/><g fill="#4a7d05"><rect x="58" y="28" width="3" height="38"/><rect x="67" y="28" width="3" height="38"/><rect x="76" y="28" width="3" height="38"/></g><circle cx="96" cy="36" r="3"/><circle cx="102" cy="46" r="2.5"/><circle cx="96" cy="56" r="3"/><circle cx="104" cy="62" r="2"/></svg>
    </div></div>
    <div class="label">Waste Collection</div><div class="bar"></div>
  </div>

  <div class="step" style="left:383px">
    <div class="ring"><div class="disc">
      <svg width="70" height="80" viewBox="0 0 70 80" fill="#fff"><rect x="6" y="10" width="58" height="8" rx="2"/><rect x="25" y="3" width="20" height="7" rx="2"/><path d="M10 21h50l-4 56H14z"/><path d="M35 36l-8 12h16z" fill="#4a7d05"/><circle cx="35" cy="55" r="10" fill="none" stroke="#4a7d05" stroke-width="3"/></svg>
    </div></div>
    <div class="label">Distributed Recycling</div><div class="bar"></div>
  </div>

  <div class="step" style="left:630px">
    <div class="ring"><div class="disc">
      <svg width="96" height="70" viewBox="0 0 96 70" fill="#fff"><path d="M4 14h56v36H4z"/><path d="M62 26h18l12 14v10H62z"/><path d="M67 30h11l7 9H67z" fill="#4a7d05"/><circle cx="20" cy="56" r="8"/><circle cx="76" cy="56" r="8"/><circle cx="20" cy="56" r="3" fill="#4a7d05"/><circle cx="76" cy="56" r="3" fill="#4a7d05"/><g fill="#4a7d05"><rect x="10" y="20" width="8" height="8"/><rect x="22" y="22" width="10" height="6"/><rect x="36" y="20" width="8" height="9"/><rect x="48" y="21" width="7" height="7"/></g><rect x="8" y="4" width="10" height="8"/><rect x="22" y="2" width="8" height="10"/><rect x="34" y="5" width="12" height="7"/></svg>
    </div></div>
    <div class="label">Waste Sorting</div><div class="bar"></div>
  </div>

  <div class="step" style="left:878px">
    <div class="ring"><div class="disc">
      <svg width="96" height="70" viewBox="0 0 96 70" fill="#fff"><rect x="4" y="26" width="88" height="7" rx="2"/><path d="M10 36h76l-10 28H20z"/><path d="M48 6l-7 11h14z"/><circle cx="48" cy="14" r="8" fill="none" stroke="#fff" stroke-width="3"/></svg>
    </div></div>
    <div class="label">Waste Rinsing</div><div class="bar"></div>
  </div>
</section>

<section class="welcome">
  <h2 class="heading" style="top:40px">WELCOME TO <span>FERNWICK4LOOP</span></h2>
  <div class="divider" style="top:88px"><i style="width:296px"></i><b></b><i style="width:296px"></i></div>
  <p>Lorem ipsum dolor sit amet, consectetuer adipiscing elit, sed diam nonummy nibh euismod tincidunt ut laoreet dolore magna aliquam erat volutpat. Ut wisi enim ad minim veniam, quis nostrud exerci tation ullamcorper suscipit lobortis nisl ut aliquip ex ea commodo consequat. Duis autem vel eum iriure dolor in hendrerit in vulputate velit esse molestie consequat, vel illum dolore eu feugiat nulla facilisis at vero eros et accumsan et iusto odio dignissim qui blandit praesent luptatum .</p>
  <div class="btn-more"><span class="txt">Read More</span><span class="arr">»</span></div>
</section>

<section class="services">
  <h2 class="heading" style="top:34px">OUR <span>SERVICES</span></h2>
  <div class="divider" style="top:82px"><i style="width:136px"></i><b></b><i style="width:136px"></i></div>

  <svg class="chev" style="left:72px" width="30" height="52" viewBox="0 0 30 52"><path d="M27 2L4 26l23 24" fill="none" stroke="#777" stroke-width="2.5"/></svg>
  <svg class="chev" style="left:1096px" width="30" height="52" viewBox="0 0 30 52"><path d="M3 2l23 24L3 50" fill="none" stroke="#777" stroke-width="2.5"/></svg>

  <div class="service" style="left:133px">
    <div class="photo" role="img" aria-label="Photo of a recycling plant with a conveyor belt and yellow railings" style="background:linear-gradient(160deg,#5c6d86,#c9c46a 55%,#3a4b62)"></div>
    <div class="title">Waste Management</div>
  </div>
  <div class="service" style="left:460px">
    <div class="photo" role="img" aria-label="Photo of a heap of discarded food containers and food scraps" style="background:linear-gradient(160deg,#b8a89a,#e8e2d8 50%,#c4493a)"></div>
    <div class="title">Food Recycling</div>
  </div>
  <div class="service" style="left:787px">
    <div class="photo" role="img" aria-label="Photo of an orange excavator demolishing a building beside trees" style="background:linear-gradient(170deg,#9fb8d6,#7a9c5d 45%,#a59a8d)"></div>
    <div class="title">Construction Recycling</div>
  </div>
</section>

<section class="blog">
  <h2 class="heading" style="top:34px">OUR <span>BLOG</span></h2>
  <div class="divider" style="top:82px"><i style="width:136px"></i><b></b><i style="width:136px"></i></div>

  <article class="post" style="left:130px">
    <div class="photo" role="img" aria-label="Photo of a red refuse truck with blue wheelie bins" style="background:linear-gradient(150deg,#6d8aa3,#a8423a 50%,#2f6aa8)"></div>
    <div class="body">
      <h3>Lorem Ipsum Dolor</h3>
      <div class="date"><svg width="16" height="16" viewBox="0 0 16 16"><circle cx="8" cy="8" r="6.5" fill="none" stroke="#4a7d05" stroke-width="1.6"/><path d="M8 4v4l3 2" fill="none" stroke="#4a7d05" stroke-width="1.6"/></svg>June 9, 2014</div>
      <p>Lorem ipsum dolor sit amet, consec tetuer adip iscing elit, sed diam nonummy nibh eu</p>
      <span class="read">Read More</span>
    </div>
  </article>

  <article class="post" style="left:618px">
    <div class="photo" role="img" aria-label="Photo of four colored recycling bins against a concrete wall" style="background:linear-gradient(90deg,#b9c2c6,#5a3f36 35%,#b8262b 65%,#2d7fb8)"></div>
    <div class="body">
      <h3>Lorem Ipsum Dolor</h3>
      <div class="date"><svg width="16" height="16" viewBox="0 0 16 16"><circle cx="8" cy="8" r="6.5" fill="none" stroke="#4a7d05" stroke-width="1.6"/><path d="M8 4v4l3 2" fill="none" stroke="#4a7d05" stroke-width="1.6"/></svg>June 9, 2014</div>
      <p>Lorem ipsum dolor sit amet, consec tetuer adip iscing elit, sed diam nonummy nibh eu</p>
      <span class="read">Read More</span>
    </div>
  </article>
</section>

<footer class="footer">
  <div class="col" style="left:132px">
    <h4>Quick Links</h4>
    <ul class="links"><li>Home</li><li>About</li><li>Services</li><li>Insight</li><li>Work</li><li>Collaborations</li><li>Blog</li><li>Contact</li></ul>
  </div>
  <div class="col" style="left:336px">
    <h4 style="width:160px">Newsletter Sign Up</h4>
    <p>Stay updated with latest news from<br>Harbor Blade Works.</p>
    <div class="email-box"><svg width="14" height="10" viewBox="0 0 14 10"><rect x=".5" y=".5" width="13" height="9" fill="none" stroke="#999"/><path d="M1 1l6 5 6-5" fill="none" stroke="#999"/></svg>Enter your Email</div>
    <span class="subscribe">SUBSCRIBE</span>
  </div>
  <div class="col" style="left:662px">
    <h4 style="width:192px">Contact Information</h4>
    <p><strong style="color:#fff;font-weight:400">Fernwick4Loop</strong><br><span style="color:#aaa">Lorem ipsum dolor sit amet,<br>consec tetuer adip iscing</span></p>
    <div class="contact-row"><svg width="14" height="14" viewBox="0 0 14 14"><path d="M2 1.5c.5-.5 1.2-.5 1.6 0l1.3 1.6c.3.4.2 1-.2 1.3l-.7.5c.7 1.6 2 2.9 3.6 3.6l.5-.7c.3-.4.9-.5 1.3-.2l1.6 1.3c.5.4.5 1.1 0 1.6l-.9.9C5.5 11 1.3 6.8 1.1 2.4z" fill="#ddd"/></svg>(555)010-246</div>
    <div class="contact-row"><svg width="14" height="14" viewBox="0 0 14 14" fill="#ddd"><rect x="3" y="1" width="8" height="4"/><rect x="1" y="5" width="12" height="5" rx="1"/><rect x="3" y="9" width="8" height="4" fill="#aaa"/></svg>5550102468</div>
    <div class="contact-row"><svg width="14" height="10" viewBox="0 0 14 10"><rect width="14" height="10" fill="#ddd"/><path d="M0 0l7 6 7-6" fill="none" stroke="#252525"/></svg>info@fernwick4loop.com</div>
  </div>
  <div class="col" style="left:937px">
    <h4 style="width:130px">Follow us</h4>
    <ul class="social"><li><span class="sq"></span>Friendline</li><li><span class="sq"></span>Chirpwire</li><li><span class="sq"></span>Orbit Plus</li><li><span class="sq"></span>Workmesh</li></ul>
  </div>
</footer>

<div class="bottombar">
  <span class="inner copy">Copyright © 2015 Fernwick4Loop. All Right Reserved.</span>
  <span class="inner legal">Privacy Policy &nbsp;|&nbsp; Terms &amp; Conditions</span>
</div>

</body>
</html>
```